Business Card Design Project_Fennick&Co

Hi,

We need some business cards designed that match the branding of this website: www.fennickandco.com

They should match this branding and include a field for:

Name
Title
Email
Mobile number
Web Address

```html
<!DOCTYPE html>
<html lang="en">
<head>
<meta charset="utf-8">
<title>Fennick&amp;Co Business Card</title>
<link href="https://fonts.googleapis.com/css2?family=Jost:wght@400;500&display=swap" rel="stylesheet">
<style>
  :root {
    --backdrop: #a6a7aa;
    --card: #ffffff;
    --ink: #111111;
    --band: #c9c9c9;
  }
  * { margin: 0; padding: 0; box-sizing: border-box; }
  html, body {
    width: 1200px;
    height: 961px;
    overflow: hidden;
    background: var(--backdrop);
    font-family: "Jost", "Futura", sans-serif;
    color: var(--ink);
  }
  .card {
    position: absolute;
    left: 84px;
    top: 152px;
    width: 1029px;
    height: 656px;
    background: var(--card);
  }
  .contact-block {
    position: absolute;
    left: 584px;
    top: 66px;
  }
  .person-name {
    font-size: 31px;
    font-weight: 500;
    line-height: 1;
  }
  .person-title {
    margin-top: 12px;
    font-size: 26px;
    font-weight: 400;
    line-height: 1;
  }
  .contact-list {
    list-style: none;
    margin-top: 54px;
  }
  .contact-item {
    display: flex;
    align-items: center;
    height: 48px;
    font-size: 28px;
    font-weight: 400;
  }
  .contact-badge {
    width: 27px;
    height: 27px;
    margin-right: 25px;
    flex-shrink: 0;
  }
  .divider-band {
    position: absolute;
    left: 0;
    top: 508px;
    width: 1026px;
    height: 12px;
    background: var(--band);
  }
  .brand {
    position: absolute;
    left: 53px;
    top: 480px;
    height: 68px;
    padding: 0 28px;
    display: flex;
    align-items: center;
    gap: 16px;
    background: var(--card);
  }
  .brand-mark {
    width: 18px;
    height: 18px;
    background: var(--ink);
  }
  .brand-name {
    font-size: 40px;
    font-weight: 500;
    letter-spacing: 1px;
    line-height: 1;
  }
</style>
</head>
<body>
  <main class="card">
    <section class="contact-block">
      <h1 class="person-name">Mara Leclair</h1>
      <p class="person-title">Sales Manager</p>
      <ul class="contact-list">
        <li class="contact-item">
          <svg class="contact-badge" viewBox="0 0 27 27" aria-hidden="true">
            <circle cx="13.5" cy="13.5" r="13.5" fill="#111111"/>
            <text x="13.5" y="18" text-anchor="middle" font-family="Jost, sans-serif" font-weight="500" font-size="12" fill="#ffffff">M</text>
          </svg>
          <span>(12) 987.654.321</span>
        </li>
        <li class="contact-item">
          <svg class="contact-badge" viewBox="0 0 27 27" aria-hidden="true">
            <circle cx="13.5" cy="13.5" r="13.5" fill="#111111"/>
            <text x="13.5" y="18" text-anchor="middle" font-family="Jost, sans-serif" font-weight="500" font-size="12" fill="#ffffff">E</text>
          </svg>
          <span>mara.l@fennickandco.com</span>
        </li>
        <li class="contact-item">
          <svg class="contact-badge" viewBox="0 0 27 27" aria-hidden="true">
            <circle cx="13.5" cy="13.5" r="13.5" fill="#111111"/>
            <text x="13.5" y="18" text-anchor="middle" font-family="Jost, sans-serif" font-weight="500" font-size="12" fill="#ffffff">W</text>
          </svg>
          <span>www.fennickandco.com</span>
        </li>
      </ul>
    </section>

    <div class="divider-band" role="img" aria-label="Decorative diamond chain border running across the card"></div>

    <div class="brand">
      <span class="brand-mark" aria-hidden="true"></span>
      <span class="brand-name">FENNICK &amp; CO</span>
    </div>
  </main>
</body>
</html>
```